Decorative concrete business needs new business cards

Our company attracts homeowners and business with disposable cash. We are a artistic decorative coatings company that will transform your driveway, patio, floors or counter tops into a work of art. We also engrave logos and designs right into the concrete! We are upscale and very professional company. I am open for rearranging our logo on the business card and also to different color patterns. We like the blue and black as in Brandquill's logo. We also like blue and orange/yellow.

Target Market(s)

Adults 30-70

Industry/Entity Type

Concrete

Contact Information for Business Card

Simple: Name, phone, email, website and social media icons

Font styles to use
Serif

Colors

Designer to choose colors to be used in the design.

Requirements
Must have
• Must present a professional upscale appearance. I have attached before and after photos that show you what our industry does. Maybe I will have before and after photo on back of card.
Nice to have
• Artistic, but bold. Nothing whimsical or cute.
Should not have
• Should not have cartoon or childlike appearance.

```html
<!DOCTYPE html>
<html lang="en">
<head>
<meta charset="utf-8">
<title>Stonecrest Surface Art – Business Cards</title>
<link rel="stylesheet" href="https://fonts.googleapis.com/css2?family=Tinos:wght@400;700&display=swap">
<style>
  :root {
    --page-bg: #e6e6e6;
    --card-white: #ffffff;
    --ink: #1a1a1a;
    --ink-soft: #555555;
    --ghost: #f1f1f1;
    --photo-dark: #4a3d2c;
    --photo-mid: #7a6548;
    --photo-light: #9a8464;
    --social: #7a7a7a;
  }
  * { box-sizing: border-box; margin: 0; padding: 0; }
  html, body { width: 1200px; height: 1200px; overflow: hidden; }
  body {
    background: var(--page-bg);
    font-family: "Tinos", "Times New Roman", serif;
    color: var(--ink);
    position: relative;
  }
  .card {
    position: absolute;
    width: 640px;
    height: 366px;
    border-radius: 4px;
    overflow: hidden;
    box-shadow: 0 10px 24px rgba(0,0,0,.18);
  }
  /* back side */
  .card--back { left: 70px; top: 120px; }
  .card-back__photo {
    position: absolute; inset: 0;
    background: linear-gradient(180deg, var(--photo-light) 0%, var(--photo-mid) 45%, var(--photo-dark) 100%);
  }
  .card-back__brand {
    position: absolute; right: 44px; bottom: 110px;
    display: flex; align-items: center; gap: 12px;
    color: var(--card-white);
    font-size: 30px; letter-spacing: 1px; text-transform: uppercase;
  }
  .card-back__social { position: absolute; right: 44px; bottom: 168px; display: flex; gap: 6px; }
  .card-back__social span { width: 20px; height: 20px; border-radius: 4px; background: rgba(255,255,255,.75); }

  /* front side */
  .card--front { left: 490px; top: 650px; background: var(--card-white); }
  .card-front__ghost {
    position: absolute; right: -40px; top: -30px;
    width: 300px; height: 300px; background: var(--ghost);
  }
  .brand {
    position: absolute; left: 44px; top: 52px;
    display: flex; align-items: center; gap: 14px;
    font-size: 34px; letter-spacing: 1px; text-transform: uppercase; color: var(--ink);
  }
  .brand__mark { width: 40px; height: 40px; background: var(--ink); }
  .card-back__brand .brand__mark { width: 34px; height: 34px; background: var(--card-white); }
  .person { position: absolute; left: 44px; top: 150px; }
  .person__name { font-size: 30px; text-transform: uppercase; letter-spacing: .5px; }
  .person__title { font-size: 18px; color: var(--ink-soft); margin-top: 2px; }
  .contacts { position: absolute; left: 44px; top: 240px; list-style: none; }
  .contacts li { display: flex; align-items: center; gap: 12px; font-size: 18px; color: var(--ink-soft); margin-bottom: 9px; }
  .contacts svg { width: 18px; height: 18px; flex: none; }
  .social { position: absolute; right: 40px; top: 170px; display: flex; gap: 8px; }
  .social span { width: 32px; height: 32px; border-radius: 6px; background: var(--social); }
</style>
</head>
<body>

<section class="card card--back" aria-label="Card back">
  <div class="card-back__photo" role="img" aria-label="Photograph of a finished decorative concrete driveway in front of a house garage with trees"></div>
  <div class="card-back__social" aria-label="Social media">
    <span></span><span></span><span></span>
  </div>
  <div class="card-back__brand"><span class="brand__mark"></span>Stonecrest Surface Art</div>
</section>

<section class="card card--front" aria-label="Card front">
  <div class="card-front__ghost"></div>
  <div class="brand"><span class="brand__mark"></span>Stonecrest Surface Art</div>
  <div class="social" aria-label="Social media">
    <span></span><span></span><span></span>
  </div>
  <div class="person">
    <div class="person__name">Alex Morgan</div>
    <div class="person__title">Director</div>
  </div>
  <ul class="contacts">
    <li>
      <svg viewBox="0 0 24 24" aria-hidden="true"><path fill="#1a1a1a" d="M6.6 10.8a15 15 0 0 0 6.6 6.6l2.2-2.2a1 1 0 0 1 1-.25 11.4 11.4 0 0 0 3.6.57 1 1 0 0 1 1 1V20a1 1 0 0 1-1 1A17 17 0 0 1 3 4a1 1 0 0 1 1-1h3.5a1 1 0 0 1 1 1c0 1.25.2 2.45.57 3.57a1 1 0 0 1-.25 1z"/></svg>
      555-014-2290
    </li>
    <li>
      <svg viewBox="0 0 24 24" aria-hidden="true" fill="none" stroke="#1a1a1a" stroke-width="1.8"><circle cx="12" cy="12" r="9"/><ellipse cx="12" cy="12" rx="4" ry="9"/><path d="M3 12h18M5 7h14M5 17h14"/></svg>
      www.stonecrestsurfaceart.com
    </li>
    <li>
      <svg viewBox="0 0 24 24" aria-hidden="true"><rect x="2" y="5" width="20" height="14" fill="#1a1a1a"/><path d="M2 5l10 8 10-8" fill="none" stroke="#fff" stroke-width="1.6"/></svg>
      alex@stonecrestsurfaceart.com
    </li>
  </ul>
</section>

</body>
</html>
```